Web Design Project

I'm seeking a web designer that will design an elegant website for my Online Portfolio
I myself am a graphic designer, But web isn't my prime field. Ill need it to be
User interface friendly with zero complexity. I will provide all the files needed, and will also
Contribute to the graphics if needed. 3D style gallery feature would be nice but not essential
giving the website look a more virtual feel to its design feature. The overall design must have a multi-tech feel to it
but nothing overboard keeping it simple. Just be creative ;-)

THIS IS A CODED WEB SITE NOT ONLY DESIGN!!!

A quick intro would be nice, no more than 5 seconds using my logo and font and some of my designs.
My designs are mostly interface audio players and digital designs.
I am looking forward for a long term collaboration,as I will constantly need an update on my website.so its not
a one off thing.

Anything you need to add that I have forgot e-mail me!

•website must be php dynamic data base.
•colour scheme:Dark Grey,black,Blue, white,
•Ill be taking a new photo,this one is only an example to work on.

Examples:

http://morvel4417.pixelnook.example/art/corsica-banjo-fresh-layout-581903744
http://trevino.pixelnook.example/art/52-Studio-730481256
http://pavlik7form.pixelnook.example/art/Pavlikform-2013-815370492
http://trevino.pixelnook.example/art/Personal-Portfolio-V1-562019837

Links for the files:

http://www.filecrate.example/zip/x42m801q/About.html
http://www.filecrate.example/zip/7KDLw3rz/Tessavine_font__logo.html
http://www.filecrate.example/zip/RbhwNqeZ/Portfolio.html
http://www.filecrate.example/zip/JtvodQke/Resources.html
http://www.filecrate.example/zip/gHWzacnp/Example_Photo.html

Target Market(s)

Design companies to be able to click onto the link of my website and see a nice design set up for my portfolio.

Industry/Entity Type

Digital

Requirements
Must have
• Be creative
Nice to have
• A short intro
3D gallery,simple style navigation,nothing ultra complicated.
Should not have
• 1)Any pictures of any kind of anyone else's art work, except if you include an abstract image having no complications with copyrights as you should know.
2)No music
3)lots of colours no more than 4 colours maximum 6 colour layout.

```html
<!DOCTYPE html>
<html lang="en">
<head>
<meta charset="utf-8">
<title>Tessavine — Portfolio</title>
<link rel="stylesheet" href="https://fonts.googleapis.com/css2?family=Fira+Sans+Condensed:wght@400;500;600&family=Source+Sans+3:wght@300;400;600&display=swap">
<style>
  :root {
    --cyan: #0ec3e3;
    --cyan-pale: #bdf1fa;
    --teal-dark: #0a4a5c;
    --teal-deep: #083d4c;
    --ink: #2e2e2e;
    --grey-text: #666;
    --white: #ffffff;
    --social: #0b8ccf;
  }
  * { margin: 0; padding: 0; box-sizing: border-box; }
  html, body { width: 1200px; height: 1053px; overflow: hidden; background: var(--white); }
  body { position: relative; font-family: "Source Sans 3", Arial, sans-serif; color: var(--ink); }
  .layer { position: absolute; left: 0; top: 0; }
  .abs { position: absolute; }

  .brand { left: 48px; top: 52px; }
  .brand-name { font-family: "Fira Sans Condensed", Arial, sans-serif; font-weight: 500; font-size: 38px; letter-spacing: 6px; color: #151515; line-height: 1; }
  .brand-slogan { font-weight: 400; font-size: 16px; letter-spacing: 2.6px; color: #777; margin-top: 8px; }

  .main-nav { left: 0; top: 50px; width: 1200px; height: 57px; }
  .main-nav a { position: absolute; top: 20px; font-family: "Fira Sans Condensed", Arial, sans-serif; font-size: 17px; color: var(--white); text-decoration: none; white-space: nowrap; }

  .hero-tag { left: 639px; top: 200px; font-family: "Fira Sans Condensed", Arial, sans-serif; font-weight: 600; font-size: 32px; color: var(--teal-dark); white-space: nowrap; }
  .hero-title { left: 639px; top: 244px; font-family: "Fira Sans Condensed", Arial, sans-serif; font-weight: 600; font-size: 57px; color: var(--white); letter-spacing: -0.5px; white-space: nowrap; }
  .hero-text { left: 649px; top: 322px; width: 470px; font-weight: 300; font-size: 16px; line-height: 24.5px; color: var(--teal-deep); }
  .hero-button { left: 649px; top: 407px; width: 111px; height: 43px; border-radius: 22px; background: var(--teal-dark); color: var(--white); font-size: 14.5px; font-weight: 400; display: flex; align-items: center; justify-content: center; }

  .section-title { font-family: "Fira Sans Condensed", Arial, sans-serif; font-weight: 600; font-size: 23px; color: #4a4a4a; letter-spacing: -0.2px; }
  .about-title { left: 58px; top: 660px; }
  .about-lead { left: 58px; top: 697px; width: 520px; font-size: 15.5px; line-height: 25px; color: var(--ink); }
  .about-body { left: 58px; top: 757px; width: 540px; font-weight: 300; font-size: 15.5px; line-height: 24.5px; color: var(--grey-text); }
  .more-link { font-size: 14.5px; color: var(--ink); display: flex; align-items: center; gap: 4px; }
  .about-more { left: 58px; top: 878px; }

  .portfolio-title { left: 876px; top: 655px; }
  .portfolio-more { left: 1069px; top: 899px; }

  .footer-note { left: 53px; top: 988px; font-weight: 300; font-size: 13.5px; color: #666; }
</style>
</head>
<body>

<svg class="layer" width="1200" height="1053" viewBox="0 0 1200 1053">
  <defs>
    <linearGradient id="heroFill" x1="0" y1="0" x2="1" y2="1">
      <stop offset="0" stop-color="#10c8e6"/>
      <stop offset="1" stop-color="#0fd6ee"/>
    </linearGradient>
    <linearGradient id="navFill" x1="0" y1="0" x2="0" y2="1">
      <stop offset="0" stop-color="#0c5d72"/>
      <stop offset="1" stop-color="#094656"/>
    </linearGradient>
    <linearGradient id="portraitFill" x1="0" y1="0" x2="0" y2="1">
      <stop offset="0" stop-color="#eef0f3"/>
      <stop offset="0.45" stop-color="#d9dde3"/>
      <stop offset="0.75" stop-color="#1b1a2a"/>
      <stop offset="1" stop-color="#121120"/>
    </linearGradient>
    <linearGradient id="panelFill" x1="0" y1="0" x2="1" y2="0">
      <stop offset="0" stop-color="#f7f8f9"/>
      <stop offset="1" stop-color="#eceef0"/>
    </linearGradient>
    <linearGradient id="footerFill" x1="0" y1="0" x2="0" y2="1">
      <stop offset="0" stop-color="#e9eaeb"/>
      <stop offset="0.2" stop-color="#f3f3f3"/>
      <stop offset="1" stop-color="#f1f1f1"/>
    </linearGradient>
    <linearGradient id="artFill" x1="0" y1="0" x2="0" y2="1">
      <stop offset="0" stop-color="#ecdcd8"/>
      <stop offset="1" stop-color="#d8e2ee"/>
    </linearGradient>
    <radialGradient id="ornamentFill" cx="0.5" cy="0.5" r="0.5">
      <stop offset="0" stop-color="#e4e4e4"/>
      <stop offset="1" stop-color="#ffffff" stop-opacity="0"/>
    </radialGradient>
    <radialGradient id="heroOrnament" cx="0.5" cy="0.5" r="0.5">
      <stop offset="0" stop-color="#3fe0f4" stop-opacity="0.55"/>
      <stop offset="1" stop-color="#0fd0ea" stop-opacity="0"/>
    </radialGradient>
    <filter id="softShadow" x="-10%" y="-10%" width="120%" height="120%">
      <feDropShadow dx="0" dy="3" stdDeviation="5" flood-color="#000" flood-opacity="0.18"/>
    </filter>
  </defs>

  <polygon points="221,0 1200,0 1200,589 609,589" fill="var(--cyan-pale)"/>
  <polygon points="238,0 1200,0 1200,589 627,589" fill="url(#heroFill)"/>
  <g role="img" aria-label="Faint floral circles and butterfly decoration in pale cyan">
    <ellipse cx="1020" cy="390" rx="200" ry="180" fill="url(#heroOrnament)"/>
    <ellipse cx="1140" cy="180" rx="90" ry="110" fill="url(#heroOrnament)"/>
  </g>

  <polygon points="566,50 1200,50 1200,107 542,107" fill="url(#navFill)"/>
  <g fill="#0b5366">
    <polygon points="660,50 671,50 648,107 637,107"/>
    <polygon points="770,50 781,50 758,107 747,107"/>
    <polygon points="895,50 906,50 883,107 872,107"/>
    <polygon points="1023,50 1034,50 1011,107 1000,107"/>
  </g>

  <g role="img" aria-label="Soft grey floral swirl ornament">
    <ellipse cx="150" cy="380" rx="190" ry="230" fill="url(#ornamentFill)"/>
  </g>

  <polygon points="598,190 946,190 919,246 598,246" fill="var(--white)"/>
  <polygon points="598,190 598,246 487,293" fill="#eef2f3"/>

  <g filter="url(#softShadow)">
    <rect x="-173" y="-173" width="346" height="346" rx="16" transform="translate(328 374) rotate(45)" fill="var(--white)"/>
  </g>
  <rect x="-162" y="-162" width="324" height="324" rx="10" transform="translate(328 374) rotate(45)" fill="#e7e9ec"/>
  <rect role="img" aria-label="Portrait photo of the designer" x="-156" y="-156" width="312" height="312" rx="8" transform="translate(328 374) rotate(45)" fill="url(#portraitFill)"/>

  <polygon points="875,589 1200,589 1200,954 631,954" fill="url(#panelFill)"/>

  <rect role="img" aria-label="Colourful bird illustration" x="612" y="628" width="160" height="226" rx="6" fill="url(#artFill)"/>

  <g>
    <rect x="870" y="690" width="96" height="85" fill="var(--white)" stroke="#e3e3e3"/>
    <rect role="img" aria-label="Portfolio artwork" x="876" y="696" width="84" height="73" fill="#4aa7b5"/>
    <rect x="969" y="690" width="96" height="85" fill="var(--white)" stroke="#e3e3e3"/>
    <rect role="img" aria-label="Portfolio artwork" x="975" y="696" width="84" height="73" fill="#b7d15a"/>
    <rect x="1068" y="690" width="96" height="85" fill="var(--white)" stroke="#e3e3e3"/>
    <rect role="img" aria-label="Portfolio artwork" x="1074" y="696" width="84" height="73" fill="#e7743b"/>
    <rect x="870" y="788" width="96" height="85" fill="var(--white)" stroke="#e3e3e3"/>
    <rect role="img" aria-label="Portfolio artwork" x="876" y="794" width="84" height="73" fill="#c46bc4"/>
    <rect x="969" y="788" width="96" height="85" fill="var(--white)" stroke="#e3e3e3"/>
    <rect role="img" aria-label="Portfolio artwork" x="975" y="794" width="84" height="73" fill="#8fc6b0"/>
    <rect x="1068" y="788" width="96" height="85" fill="var(--white)" stroke="#e3e3e3"/>
    <rect role="img" aria-label="Portfolio artwork" x="1074" y="794" width="84" height="73" fill="#78b8d8"/>
  </g>

  <g fill="none" stroke="var(--white)" stroke-width="2.2" stroke-linecap="round" stroke-linejoin="round">
    <polyline points="641,527 629,539 641,551"/>
    <polyline points="666,527 678,539 666,551"/>
  </g>

  <rect x="0" y="954" width="1200" height="99" fill="url(#footerFill)"/>
  <g fill="var(--social)">
    <circle cx="1047" cy="992" r="13"/>
    <circle cx="1076" cy="992" r="13"/>
    <circle cx="1106" cy="992" r="13"/>
    <circle cx="1136" cy="992" r="13"/>
  </g>
</svg>

<div class="abs brand">
  <div class="brand-name">TESSAVINE</div>
  <div class="brand-slogan">SLOGAN GOES HERE</div>
</div>

<nav class="abs main-nav">
  <a href="#" style="left:604px">MAIN</a>
  <a href="#" style="left:682px">ABOUT US</a>
  <a href="#" style="left:793px">PORTFOLIO</a>
  <a href="#" style="left:915px">BLOG POST</a>
  <a href="#" style="left:1043px">CONTACT ME</a>
</nav>

<div class="abs hero-tag">Welcome to My</div>
<div class="abs hero-title">Website Mainpage..</div>
<p class="abs hero-text">Duis tincidunt lectus quis dui viverra vestibulum. Suspendisse vulputate aliquam dui. Nulla elemenum dui ut augue. Aliquam vehicula mi at mauris nisl at consequat rhoncus,</p>
<div class="abs hero-button">View Project</div>

<h2 class="abs section-title about-title">LITTLE ABOUT MY SELF</h2>
<p class="abs about-lead">Nunc tempus felis vitae urna. Vivamus porttitor, g, purus nisi eleifend libero, a tempus libero lectus feugiat felis.</p>
<p class="abs about-body">Morbi eget arcu. Morbi porta, libero id ullamcorper nonummy, nibh ligula pulvinar metus, eget consectetuer augue nisi quis lacus. Ut ac mi quis lacus mollis aliquam. Curabitur iaculis tempus eros. Curabitur vel mi sit amet magna malesuada ultrices. Ut nisi erat, fermentum vel,</p>
<div class="abs more-link about-more">Learn More
  <svg width="8" height="10" viewBox="0 0 8 10"><polyline points="2,1 6,5 2,9" fill="none" stroke="#222" stroke-width="2"/></svg>
</div>

<h2 class="abs section-title portfolio-title">MY PORTFOLIO</h2>
<div class="abs more-link portfolio-more">View More
  <svg width="8" height="10" viewBox="0 0 8 10"><polyline points="2,1 6,5 2,9" fill="none" stroke="#222" stroke-width="2"/></svg>
</div>

<div class="abs footer-note">© 2012 Company Name.&nbsp; All right reserved.&nbsp; Term of Use</div>

</body>
</html>
```